"Harrow Crest Builders" is a residential building company and needs a new business card design and may re

We would like a redesign based on the existing logo, and would like to see a new font as well. We are bespoke home builders who build sustainable energy efficient homes.

Industry/Entity Type

Construction

Contact Information for Business Card

Business card size 40mm x 90mm

Colors

Designer to choose colors to be used in the design.

```html
<!DOCTYPE html>
<html lang="en">
<head>
<meta charset="utf-8">
<title>Harrow Crest Builders – Business Card</title>
<link rel="stylesheet" href="https://fonts.googleapis.com/css2?family=Montserrat:wght@400;600&family=Arimo:wght@700&display=swap">
<style>
  :root {
    --page: #ffffff;
    --brand-green: #8dc63f;
    --brand-grey: #808285;
    --frame-grey: #8a8a8a;
    --ink: #111111;
    --icon: #8a8a8a;
    --white: #ffffff;
  }
  * { margin: 0; padding: 0; box-sizing: border-box; }
  html, body {
    width: 1200px; height: 1000px; overflow: hidden;
    background: var(--page);
    font-family: "Montserrat", Arial, sans-serif;
  }
  .canvas { position: relative; width: 1200px; height: 1000px; }

  .card { position: absolute; left: 331px; width: 538px; height: 324px; }
  .card--front { top: 164px; border: 2px solid var(--frame-grey); background: var(--white); }
  .card--back { top: 513px; height: 322px; background: var(--brand-green); }

  .brand { position: absolute; display: flex; align-items: center; }
  .brand__dot { flex: none; border-radius: 50%; }
  .brand__name { font-weight: 600; letter-spacing: -0.5px; }

  .card--front .brand { right: 40px; top: 30px; gap: 10px; }
  .card--front .brand__dot { width: 52px; height: 52px; background: var(--brand-green); }
  .card--front .brand__name { color: var(--brand-green); font-size: 30px; line-height: 32px; }

  .card--back .brand { left: 50%; top: 50%; transform: translate(-50%, -50%); gap: 22px; }
  .card--back .brand__dot { width: 84px; height: 84px; background: var(--white); }
  .card--back .brand__name { color: var(--white); font-size: 50px; line-height: 56px; }

  .contact { position: absolute; left: 22px; top: 176px; }
  .contact__name {
    font-family: "Arimo", Arial, sans-serif; font-weight: 700;
    font-size: 19px; color: var(--ink); margin-left: 2px; margin-bottom: 3px;
  }
  .contact__list { list-style: none; }
  .contact__item {
    display: flex; align-items: center; gap: 4px;
    font-size: 15.5px; line-height: 20.3px; color: var(--ink);
  }
  .contact__item--plain { padding-left: 16px; }
  .contact__icon { width: 12px; height: 12px; flex: none; fill: var(--icon); }
</style>
</head>
<body>
<main class="canvas">
  <section class="card card--front" aria-label="Card front">
    <div class="brand">
      <span class="brand__dot"></span>
      <span class="brand__name">harrow crest<br>builders</span>
    </div>
    <div class="contact">
      <p class="contact__name">Daniel Ferrante</p>
      <ul class="contact__list">
        <li class="contact__item">
          <svg class="contact__icon" viewBox="0 0 12 12"><rect x="3" y="0.5" width="6" height="11" rx="1.2"/><rect x="4.2" y="2" width="3.6" height="3.5" fill="#fff"/></svg>
          0400 118 362
        </li>
        <li class="contact__item">
          <svg class="contact__icon" viewBox="0 0 12 12"><rect x="0.5" y="2.5" width="11" height="7.5" rx="0.8"/><path d="M1 3l5 3.6L11 3" stroke="#fff" stroke-width="1" fill="none"/></svg>
          daniel@harrowcrestbuilders.com.au
        </li>
        <li class="contact__item">
          <svg class="contact__icon" viewBox="0 0 12 12"><g fill="none" stroke="#8a8a8a" stroke-width="1"><circle cx="6" cy="6" r="5"/><ellipse cx="6" cy="6" rx="2.2" ry="5"/><path d="M1 6h10M2 3.3h8M2 8.7h8"/></g></svg>
          www.harrowcrestbuilders.com.au
        </li>
        <li class="contact__item">
          <svg class="contact__icon" viewBox="0 0 12 12"><path d="M6 0.5a4 4 0 0 1 4 4c0 3-4 7-4 7s-4-4-4-7a4 4 0 0 1 4-4z"/><circle cx="6" cy="4.5" r="1.4" fill="#fff"/></svg>
          PO Box 7142 Northgate LPO Kelmscott WA 6111
        </li>
        <li class="contact__item contact__item--plain">Registration 48213 ABN: 52 904 316 778</li>
      </ul>
    </div>
  </section>

  <section class="card card--back" aria-label="Card back">
    <div class="brand">
      <span class="brand__dot"></span>
      <span class="brand__name">harrow crest<br>builders</span>
    </div>
  </section>
</main>
</body>
</html>
```